Business card design needed

Marketing Communications

Target Market(s)

prospective clients in the marketing communications industry

Industry/Entity Type

Business

Contact Information for Business Card

merel vasko
Marketing Communications
tolupar@quennet.com
0462 815947

Logo Text

merel vasko

Logo styles of interest
Abstract Logo
Requirements
Must have
• An appropriate abstract logo. only a one or two colour design
Nice to have
• Logo to portray the growth of a marketing brief
Should not have
• no more than two colours maximum

```html
<!DOCTYPE html>
<html lang="en">
<head>
<meta charset="utf-8">
<title>Merel Vasko — Business Card</title>
<link rel="stylesheet" href="https://fonts.googleapis.com/css2?family=Roboto+Condensed:wght@400&display=swap">
<style>
  :root {
    --page: #ffffff;
    --frame: #1a1a1a;
    --card: #201c1a;
    --ink: #ffffff;
    --muted: #9a9694;
    --accent: #a6d0e0;
  }
  html, body {
    margin: 0;
    padding: 0;
    width: 1200px;
    height: 694px;
    overflow: hidden;
    background: var(--page);
  }
  .canvas {
    position: relative;
    width: 1200px;
    height: 694px;
    font-family: "Roboto Condensed", "Arial Narrow", sans-serif;
  }
  .frame {
    position: absolute;
    left: 20px;
    top: 20px;
    width: 1158px;
    height: 667px;
    box-sizing: border-box;
    border: 3px solid var(--frame);
    border-radius: 2px;
  }
  .card {
    position: absolute;
    left: 48px;
    top: 48px;
    width: 1102px;
    height: 612px;
    background: var(--card);
  }
  .divider {
    position: absolute;
    left: 602px;
    width: 12px;
  }
  .divider--accent { top: 0; height: 430px; background: var(--accent); }
  .divider--light { top: 503px; height: 109px; background: var(--ink); }

  .contact {
    position: absolute;
    right: 529px;
    text-align: right;
    margin: 0;
  }
  .contact__value {
    display: block;
    color: var(--ink);
    font-size: 33px;
    line-height: 1;
    letter-spacing: 0.2px;
  }
  .contact__label {
    display: block;
    color: var(--muted);
    font-size: 18px;
    line-height: 1;
    margin-top: 6px;
  }
  .contact--email { top: 195px; }
  .contact--phone { top: 295px; }

  .identity {
    position: absolute;
    left: 640px;
    top: 190px;
  }
  .identity__name {
    margin: 0;
    color: var(--ink);
    font-weight: 400;
    font-size: 66px;
    line-height: 1;
    text-transform: uppercase;
    letter-spacing: 0.5px;
  }
  .identity__role {
    margin: 14px 0 0 2px;
    color: var(--muted);
    font-size: 20px;
    line-height: 1;
    text-transform: uppercase;
  }
</style>
</head>
<body>
  <div class="canvas">
    <div class="frame"></div>
    <section class="card">
      <div class="divider divider--accent"></div>
      <div class="divider divider--light"></div>

      <p class="contact contact--email">
        <span class="contact__value">tolupar@quennet.com</span>
        <span class="contact__label">email</span>
      </p>
      <p class="contact contact--phone">
        <span class="contact__value">0462 815947</span>
        <span class="contact__label">phone</span>
      </p>

      <div class="identity">
        <h1 class="identity__name">Merel Vasko</h1>
        <p class="identity__role">Marketing Communications</p>
      </div>
    </section>
  </div>
</body>
</html>
```